Marketing Brochure For Tallbrook LLC for marketing and advertising purposes.A slick and modern design. I have added in the attachment a PDF called Tallbrook Profile which is the old version of this new one we are creating but can give you an idea of what I am looking for. I also have a Word document called New Consulting Document that lists each topic, where the attached images go, and the wording that goes in each. The total brochure should be between 8 and 12 pages.

Industry/Entity Type

Credit Card

Font styles to use
Serif

Colors
f78f20
886aae

Requirements
Must have
• A slick and modern design. I have added in the attachment a PDF called Tallbrook Profile which is the old version of this new one we are creating but can give you an idea of what I am looking for. I also have a Word document called New Consulting Document that lists each topic, where the attached images go, and the wording that goes in each. The total brochure should be between 8 and 12 pages.

```html
<!DOCTYPE html>
<html lang="en">
<head>
<meta charset="utf-8">
<title>Tallbrook LLC Brochure</title>
<link rel="stylesheet" href="https://fonts.googleapis.com/css2?family=Oswald:wght@500;700&family=PT+Sans:wght@400;700&display=swap">
<style>
:root{
  --orange:#f78f20;
  --coral:#ef5a6f;
  --pink:#d9547f;
  --purple:#886aae;
  --ink:#1c1c1c;
  --text:#333;
  --photo-deep:#0c3d7a;
  --photo-mid:#2a6db3;
  --photo-light:#cfe0f2;
  --panel:#ececef;
  --bg:#ffffff;
}
*{margin:0;padding:0;box-sizing:border-box}
html,body{width:880px;height:1200px;overflow:hidden;background:var(--bg)}
body{position:relative;font-family:"PT Sans",sans-serif;color:var(--text)}
.page{position:absolute;width:350px;height:496px;background:#f4f6f9;overflow:hidden;box-shadow:0 2px 8px rgba(0,0,0,.25)}
.page--back{left:73px;top:73px}
.page--front{left:454px;top:73px}
.page--consulting{left:73px;top:620px}
.page--services{left:454px;top:620px}
.photo{position:absolute;left:0;top:0;width:350px}
.photo--skyward{height:420px;background:linear-gradient(160deg,var(--photo-deep) 0%,var(--photo-mid) 35%,var(--photo-light) 60%,var(--photo-mid) 80%,var(--photo-deep) 100%)}
.photo--skyline{height:380px;background:linear-gradient(180deg,#1d6fc4 0%,#0f4f96 45%,#0a2f5c 100%)}
.panel{position:absolute;left:0;top:0}
.brand{position:absolute;font-weight:700;color:var(--purple);letter-spacing:.5px;display:flex;align-items:center;gap:6px}
.brand__dot{width:12px;height:12px;border-radius:50%;background:var(--purple)}
.brand--back{left:140px;top:142px;font-size:22px}
.brand--front{left:60px;top:360px;font-size:32px}
.brand--front .brand__dot{width:18px;height:18px}
.contact__title{position:absolute;left:32px;top:404px;font-size:8.5px;color:var(--ink)}
.contact__title b{color:var(--purple);font-weight:700}
.contact__line{position:absolute;left:32px;font-size:7.5px;color:var(--ink);display:flex;align-items:center;gap:4px}
.social{position:absolute;left:262px;top:440px;display:flex;gap:5px}
.social span{width:12px;height:12px;border-radius:50%;background:var(--purple)}
.footer-line{position:absolute;left:0;top:472px;width:350px;height:1px;background:linear-gradient(90deg,var(--orange),var(--pink))}
.footer-bar{position:absolute;top:462px;width:157px;height:20px;color:#fff;font-size:7.5px;display:flex;align-items:center;gap:4px;padding:0 10px}
.footer-bar--left{left:0;background:linear-gradient(90deg,var(--orange),var(--coral))}
.footer-bar--right{right:0;justify-content:flex-end;background:linear-gradient(90deg,var(--pink),var(--orange))}
.footer-bar--left.footer-bar--purple{background:linear-gradient(90deg,var(--purple),var(--pink))}
.footer-bar--right.footer-bar--purple{background:linear-gradient(90deg,var(--pink),var(--purple))}
.footer-bar__globe{width:6px;height:6px;border:1px solid #fff;border-radius:50%}
.footer-bar b{font-weight:700}
.tagline{position:absolute;left:0;top:421px;width:350px;height:30px;background:linear-gradient(90deg,var(--pink),var(--purple));color:#fff;font-family:"Oswald",sans-serif;font-weight:500;font-size:15px;letter-spacing:.3px;display:flex;align-items:center;justify-content:center}
.tab{position:absolute;top:0;width:42px;height:58px;background:linear-gradient(180deg,var(--orange),var(--coral))}
.page-title{position:absolute;top:32px;font-family:"Oswald",sans-serif;font-weight:700;font-size:21px;color:var(--ink);letter-spacing:.4px}
.body{position:absolute;font-size:5.6px;line-height:8px;text-align:justify;color:var(--text)}
.body p+p{margin-top:7px}
.section-title{position:absolute;left:37px;font-size:11px;font-weight:700;color:var(--purple)}
.figure{position:absolute;border:3px solid #fff;box-shadow:0 0 2px rgba(0,0,0,.3)}
.figure--consulting{left:60px;top:160px;width:225px;height:80px;border:none;box-shadow:none;background:linear-gradient(180deg,#f2f3f6,#dfe2ea)}
.figure--values{left:200px;top:272px;width:125px;height:172px;border:none;box-shadow:none;background:linear-gradient(180deg,#eceaf2,#e3e6ee)}
.figure--compliance{left:200px;top:146px;width:105px;height:84px;background:linear-gradient(135deg,#f4f1f6,#d8d2e0)}
.figure--training{left:200px;top:389px;width:105px;height:64px;background:linear-gradient(135deg,#f2eee8,#e2cfc8)}
</style>
</head>
<body>

<section class="page page--back">
  <div class="photo photo--skyward" role="img" aria-label="Photo looking up at blue glass skyscrapers against a pale sky"></div>
  <svg class="panel" width="350" height="496" viewBox="0 0 350 496">
    <polygon points="0,382 130,382 155,395 178,420 270,420 350,410 350,496 0,496" fill="var(--panel)"/>
  </svg>
  <div class="brand brand--back"><span class="brand__dot"></span>Tallbrook</div>
  <div class="contact__title">CONTACT <b>US</b></div>
  <div class="contact__line" style="top:425px">
    <svg width="7" height="7" viewBox="0 0 10 10"><path d="M2 1l2 2-1 1.5a6 6 0 0 0 2.5 2.5L7 6l2 2-1.5 1.5C4.5 9.5.5 5.5.5 2.5z" fill="var(--purple)"/></svg>555-014-2738</div>
  <div class="contact__line" style="top:439px">
    <svg width="7" height="6" viewBox="0 0 10 8"><rect x=".5" y=".5" width="9" height="7" fill="none" stroke="var(--purple)"/><path d="M.5.5l4.5 4 4.5-4" fill="none" stroke="var(--purple)"/></svg>info@tallbrookco.com</div>
  <div class="social"><span></span><span></span><span></span></div>
  <div class="footer-line"></div>
  <div class="footer-bar footer-bar--left"><span class="footer-bar__globe"></span><span>www.<b>tallbrookco</b>.com</span></div>
</section>

<section class="page page--front">
  <div class="photo photo--skyline" role="img" aria-label="Photo of a blue-toned city skyline at night"></div>
  <svg class="panel" width="350" height="496" viewBox="0 0 350 496">
    <polygon points="0,318 150,330 210,355 350,355 350,496 0,496" fill="var(--panel)"/>
  </svg>
  <div class="brand brand--front"><span class="brand__dot"></span>Tallbrook</div>
  <div class="tagline">ENGAGE, INSPIRE, AND EMPOWER</div>
  <div class="footer-line"></div>
  <div class="footer-bar footer-bar--right"><span class="footer-bar__globe"></span><span>www.<b>tallbrookco</b>.com</span></div>
</section>

<section class="page page--consulting">
  <div class="tab" style="left:39px"></div>
  <h2 class="page-title" style="left:39px">CONSULTING</h2>
  <div class="body" style="left:39px;top:74px;width:272px">
    <p>Tallbrook LLC provides consulting services and specializes in the credit and collection industry. The area of focus for consulting is debt collection agencies, creditors, asset buyers, and solution providers. Our consulting services are focused on two avenues; staying ahead of the curve and turning challenging situations into positive experiences. Tallbrook offers a holistic approach to it's consulting but also offers an ala carte process by focusing in the areas of Operational Excellence, Compliance, Employee Development, Business Development, Client Experience, Information Technology, and Public Relations. Tallbrook takes great pride in getting organizations to obtain maximum output with minimum input while increasing efficiency, effectiveness, and profitability.</p>
  </div>
  <div class="figure figure--consulting" role="img" aria-label="Illustration of the word consulting with icons for goal, expert, knowledge, strategy, advice, support and success"></div>
  <div class="body" style="left:39px;top:262px;width:144px">
    <p>Tallbrook also specializes in leadership coaching with a focus on mid-level, senior, and executive level management. We have found over the years that most organizations do a good enough job in training their front line employees but fail to train the leaders that are leading the organization. That is where Tallbrook comes in, with over two decades of training all levels of employees our training program is customized to reach upper level management. We focus on where the individual or the organization wants or needs to be in order to be the most productive individually and corporately. Our program interacts with everyone on their level in a way that energizes them to achieve extraordinary results with desired objectives and goals in mind. It is important for us to identify and understand each situation and priorities of the individual and organization so that each unique situation is strategized on how to reach them while providing a learning environment that teaches them to overcome obstacles that rise along the journey. Tallbrook Leadership focus on five avenues; Mindset, Purpose, Caring, Communication, and Courage.</p>
  </div>
  <div class="figure figure--values" role="img" aria-label="Graphic of the five leadership coaching values"></div>
  <div class="footer-line"></div>
  <div class="footer-bar footer-bar--left footer-bar--purple"><span class="footer-bar__globe"></span><span>www.<b>tallbrookco</b>.com</span></div>
</section>

<section class="page page--services">
  <div class="tab" style="left:37px;width:63px"></div>
  <h2 class="page-title" style="left:37px">SERVICES PROVIDED</h2>
  <h3 class="section-title" style="top:72px">Operational Excellence</h3>
  <div class="body" style="left:37px;top:95px;width:268px">
    <p>We will provide an exhaustive and unbiased review of your organizations current collection strategies from a cradle to grave work flow standpoint. This will include best practices from across the industry and provide you with templated procedures, necessary reporting, workforce management, and ensuring your organization is working with the right technology providers at the right cost to the organization.</p>
  </div>
  <div class="body" style="left:37px;top:146px;width:150px">
    <p>We will provide an exhaustive and unbiased review of your organizations current collection strategies from a cradle to grave work flow standpoint. This will include best practices from across the industry and provide you with templated procedures, necessary reporting, workforce management, and ensuring your organization is working with the right technology providers at the right cost to the organization.</p>
    <p>If warranted, a full and complete review of the organizations profit, and loss statement would be reviewed and findings shared with executive management to identify areas and trends where the strengths and areas of opportunities are.</p>
  </div>
  <div class="figure figure--compliance" role="img" aria-label="Diagram of compliance with icons for requirements, rules, standards, governance, regulations, transparency and policies"></div>
  <h3 class="section-title" style="top:272px">Employee Development</h3>
  <div class="body" style="left:37px;top:295px;width:268px">
    <p>When it comes to any organization, the number one asset is the employees. If you take care of your employees, they will take care of your consumers, and that will take care of your organization. Ultimately, all we do starts and ends with our employees and we have developed a training curriculum from the first day all the way through years of gainful employment.</p>
    <p>Unfortunately, the debt collection industry operates under several strict liability statutes which means all employees must always be perfect. We all realize that is an unreasonable request but a request that must be adhered to nonetheless. We spend a lot of time with employees on how to operate under these statutes and what they can do to mitigate violating the various laws they must follow but still performing at optimal levels.</p>
  </div>
  <div class="body" style="left:37px;top:392px;width:150px">
    <p>We will help build a foundation and create or enhance your current employee development program which includes orientation, initial and ongoing training, employee handbooks, training manuals, and talent evaluations and reviews for each department.</p>
  </div>
  <div class="figure figure--training" role="img" aria-label="Hand drawing a people development chart linking train, educate, empower and reward"></div>
  <div class="footer-line"></div>
  <div class="footer-bar footer-bar--right footer-bar--purple"><span class="footer-bar__globe"></span><span>www.<b>tallbrookco</b>.com</span></div>
</section>

</body>
</html>
```